PowerPoint Design Project

Kestrel Estate Group is a Melbourne based property development management company. We provide a comprehensive range of development management services to a select group of listed developers, private landowners, overseas investors and development partners and institutional clients. Our website provides additional information about the company:
http://www.kestreleg.com.au
We are looking for a versatile powerpoint design that can be used across a wide variety of presentations including; pitch documents, client reports, Information memorandums, and downloadable credential packs etc. We have attached a good example document.
Updates

Industry/Entity Type

It Company

Requirements
Must have
• The design should have the following slides as a minimum: Intro Page, transition slides, profile slides, slides for graphics,

```html
<!DOCTYPE html>
<html lang="en">
<head>
<meta charset="utf-8">
<title>About Kestrel</title>
<link href="https://fonts.googleapis.com/css2?family=Exo+2:wght@300;400&family=Open+Sans:wght@400;600&family=Archivo+Narrow:wght@700&display=swap" rel="stylesheet">
<style>
  :root {
    --page-bg: #ffffff;
    --header-top: #fbfbfb;
    --header-bottom: #e4e4e4;
    --title-ink: #2c2c2c;
    --body-ink: #4a4a4a;
    --icon-dark: #555a5c;
    --icon-ring: #d9d9d9;
    --footer-band: #555a5a;
    --footer-line: #cfd1d1;
    --footer-ink: #ffffff;
    --texture: #ececec;
  }
  html, body { margin: 0; padding: 0; overflow: hidden; }
  body { width: 1200px; height: 900px; background: var(--page-bg); position: relative; font-family: "Open Sans", sans-serif; }
  .slide { position: absolute; inset: 0; overflow: hidden; }
  .header {
    position: absolute; left: 0; top: 0; width: 1200px; height: 99px;
    background: linear-gradient(180deg, var(--header-top), var(--header-bottom));
  }
  .header__title {
    position: absolute; left: 44px; top: 24px; margin: 0;
    font-family: "Exo 2", sans-serif; font-weight: 300; font-size: 40px; color: var(--title-ink); letter-spacing: 0.5px;
  }
  .header__title strong { font-weight: 400; }
  .texture {
    position: absolute; left: 640px; top: 99px; width: 560px; height: 640px;
    background: radial-gradient(ellipse at 75% 35%, var(--texture) 0%, rgba(236,236,236,0.6) 40%, rgba(255,255,255,0) 72%);
  }
  .section { position: absolute; left: 0; width: 1200px; }
  .section__head {
    position: absolute; left: 54px; top: 0; display: flex; align-items: center; margin: 0;
    font-weight: 400; font-size: 25px; color: var(--body-ink);
  }
  .section__icon { width: 44px; height: 44px; margin-right: 22px; }
  .points { list-style: none; margin: 0; padding: 0; position: absolute; left: 124px; top: 47px; }
  .point {
    position: relative; padding-left: 20px; margin-bottom: 29px;
    font-weight: 600; font-size: 18.5px; line-height: 28.5px; color: var(--body-ink); letter-spacing: -0.1px;
  }
  .point::before {
    content: ""; position: absolute; left: 0; top: 9px; width: 7px; height: 7px;
    border-right: 3px solid var(--icon-dark); border-top: 3px solid var(--icon-dark); transform: rotate(45deg);
  }
  .footer-line { position: absolute; left: 0; top: 840px; width: 1200px; height: 9px; background: var(--footer-line); }
  .footer {
    position: absolute; left: 0; top: 849px; width: 1200px; height: 51px; background: var(--footer-band);
    font-family: "Archivo Narrow", sans-serif; font-weight: 700; font-size: 21px; color: var(--footer-ink);
  }
  .footer__page { position: absolute; left: 47px; top: 12px; letter-spacing: 0.5px; }
  .footer__copy { position: absolute; right: 40px; top: 12px; letter-spacing: 0.5px; }
</style>
</head>
<body>
<main class="slide">
  <header class="header">
    <h1 class="header__title">About <strong>Kestrel</strong></h1>
  </header>

  <div class="texture" role="img" aria-label="Faint grey dotted background texture"></div>

  <section class="section" style="top:163px">
    <h2 class="section__head">
      <svg class="section__icon" viewBox="0 0 44 44" aria-hidden="true">
        <circle cx="22" cy="22" r="21" fill="var(--icon-ring)"/>
        <circle cx="22" cy="22" r="18" fill="#fff"/>
        <circle cx="22" cy="22" r="15" fill="var(--icon-dark)"/>
        <path d="M14 22h14M22 16l6 6-6 6" stroke="#fff" stroke-width="3" fill="none" stroke-linecap="round" stroke-linejoin="round"/>
      </svg>
      Lorem ipsum dolor sit ipsum Lorem ipsum dolor sit ipsum Lorem ipsum
    </h2>
    <ul class="points">
      <li class="point">Lorem ipsum dolor sit ipsum Lorem ipsum dolor sit ipsum Lorem ipsum&nbsp; Lorem ipsum dolor<br>sit ipsum Lorem ipsum dolor sit ipsum Lorem ipsum</li>
      <li class="point">Lorem ipsum dolor sit ipsum Lorem ipsum dolor sit ipsum Lorem ipsum&nbsp; Lorem ipsum dolor<br>sit ipsum Lorem ipsum dolor sit ipsum Lorem ipsum</li>
      <li class="point">Lorem ipsum dolor sit ipsum Lorem ipsum dolor sit ipsum Lorem ipsum&nbsp; Lorem ipsum dolor<br>sit ipsum Lorem ipsum dolor sit ipsum Lorem ipsum</li>
    </ul>
  </section>

  <section class="section" style="top:478px">
    <h2 class="section__head">
      <svg class="section__icon" viewBox="0 0 44 44" aria-hidden="true">
        <circle cx="22" cy="22" r="21" fill="var(--icon-ring)"/>
        <circle cx="22" cy="22" r="18" fill="#fff"/>
        <circle cx="22" cy="22" r="15" fill="var(--icon-dark)"/>
        <path d="M14 22h14M22 16l6 6-6 6" stroke="#fff" stroke-width="3" fill="none" stroke-linecap="round" stroke-linejoin="round"/>
      </svg>
      Lorem ipsum dolor sit ipsum Lorem ipsum dolor sit ipsum Lorem ipsum
    </h2>
    <ul class="points">
      <li class="point">Lorem ipsum dolor sit ipsum Lorem ipsum dolor sit ipsum Lorem ipsum&nbsp; Lorem ipsum dolor<br>sit ipsum Lorem ipsum dolor sit ipsum Lorem ipsum</li>
      <li class="point">Lorem ipsum dolor sit ipsum Lorem ipsum dolor sit ipsum Lorem ipsum&nbsp; Lorem ipsum dolor<br>sit ipsum Lorem ipsum dolor sit ipsum Lorem ipsum</li>
      <li class="point">Lorem ipsum dolor sit ipsum Lorem ipsum dolor sit ipsum Lorem ipsum&nbsp; Lorem ipsum dolor<br>sit ipsum Lorem ipsum dolor sit ipsum Lorem ipsum</li>
    </ul>
  </section>

  <div class="footer-line"></div>
  <footer class="footer">
    <span class="footer__page">Page No. 00</span>
    <span class="footer__copy">Copyright@2013</span>
  </footer>
</main>
</body>
</html>
```